LanternPips business card for creator of IP TOY (fun) (children) designs

This business card will be the introduction of me as the creator of new designs to the toy industry and beyond. These designs are kept secret until being revealed one on one to each company. My design is patent pending protected IP. I am looking for business appropriate with a tinge of fun. Please no black backgounds as this is the toy industry. Be creative with the logo and colors please. Just imagine.

Target Market(s)

TOY Industry Executives - Inventor Relations - Manufacturers this is my first introduction card.

Industry/Entity Type

Toy Industry - I have included our Brand colors which can be seen on the cover of The Quiet Pebble Moon book so uses for any of these others colors would be intersting.

Contact Information for Business Card

LOGO Mara Delwyn Founder Creator 555 017 2869 4718 E Hollin Bend Fernmoor, QX 70812 www.lanternpips-demo.com maradelwyn@quillpost-mail.com Patent Pending IP

Font styles to use
Other font styles liked:
• The font used in the logo is Swiss721BT bold I need to see other fonts to be able to decide but need a clean look

Requirements
Must have
• A bit of an artistic flair although the logo is very simple. I am in the toy industry so would like something that sparks the look of being a creator?
Nice to have
• Please try a background other than stark white. Would like to see a play using brand colors?I like the logos which look like they are lifted off the page. Then under the logo the words (not lifted?) Any Action Any Character Any Teaching
Should not have
• No Black Backgrounds please! should look as clean as possible - I am not opposed to changing to a double sided card if that is more effectual.

```html
<!DOCTYPE html>
<html lang="en">
<head>
<meta charset="utf-8">
<title>LanternPips Business Card</title>
<link rel="stylesheet" href="https://fonts.googleapis.com/css2?family=Montserrat:wght@600;700;800&family=Lato:wght@400;700&display=swap">
<style>
  :root {
    --page: #e9e9ea;
    --sky-light: #cfe3f5;
    --sky-mid: #a9cdee;
    --sky-deep: #6ea9dc;
    --brand-red: #d81f26;
    --brand-yellow: #f6c21c;
    --band-blue: #bcd8f0;
    --white: #ffffff;
    --ink: #1c1c1c;
    --fence: #f4f6f8;
    --scene-green: #8fb88a;
    --sunflower: #f2b21e;
  }
  * { box-sizing: border-box; margin: 0; padding: 0; }
  html, body {
    width: 1200px; height: 1000px; overflow: hidden;
    background: var(--page);
  }
  .canvas {
    position: relative; width: 1200px; height: 1000px;
    display: flex; flex-direction: column; align-items: center; justify-content: center; gap: 56px;
  }
  .card {
    position: relative; width: 700px; height: 400px; overflow: hidden;
    box-shadow: 0 10px 28px rgba(0,0,0,0.14);
  }

  /* Front side */
  .card--front {
    background: linear-gradient(215deg, var(--sky-deep) 0%, var(--sky-mid) 40%, var(--sky-light) 100%);
  }
  .front-logo {
    position: absolute; left: 110px; top: 120px;
    font-family: "Montserrat", sans-serif; font-weight: 800;
    font-size: 66px; letter-spacing: -1px; color: var(--brand-red);
  }
  .front-web {
    position: absolute; left: 0; right: 0; top: 228px; text-align: center;
    font-family: "Lato", sans-serif; font-weight: 700; font-size: 17px;
    letter-spacing: 3px; color: var(--ink);
  }
  .front-web .accent { color: var(--brand-red); }
  .bees {
    position: absolute; left: 470px; top: 62px; width: 90px; height: 40px;
    border-radius: 20px;
    background: linear-gradient(90deg, #f7d84a, #e9473f);
    opacity: 0.8;
  }
  .sunflowers {
    position: absolute; right: 22px; top: 150px; width: 110px; height: 150px;
    border-radius: 40px 40px 8px 8px;
    background: linear-gradient(180deg, var(--sunflower), #d98a16 70%, var(--scene-green));
    opacity: 0.9;
  }
  .fence-scene {
    position: absolute; left: 0; right: 0; bottom: 0; height: 120px;
    background: linear-gradient(180deg, rgba(255,255,255,0) 0%, var(--fence) 45%, #e4e8ec 100%);
  }
  .house {
    position: absolute; left: 40px; bottom: 20px; width: 150px; height: 110px;
    border-radius: 6px 6px 0 0;
    background: linear-gradient(180deg, #c84a3c 0%, #c84a3c 22%, #efe3c8 22%, #e6d6b4 100%);
  }

  /* Back side */
  .card--back { background: var(--brand-red); color: var(--white); }
  .back-logo {
    position: absolute; left: 52px; top: 168px;
    font-family: "Montserrat", sans-serif; font-weight: 800;
    font-size: 52px; letter-spacing: -1px; color: var(--white);
  }
  .contact {
    position: absolute; left: 400px; top: 70px; width: 280px;
  }
  .contact__name {
    font-family: "Montserrat", sans-serif; font-weight: 700; font-size: 26px;
    letter-spacing: 0.3px; text-transform: uppercase; line-height: 1.1;
  }
  .contact__title {
    margin-top: 6px;
    font-family: "Montserrat", sans-serif; font-weight: 700; font-size: 15px;
    letter-spacing: 0.5px; text-transform: uppercase;
  }
  .contact__rule {
    width: 78px; height: 1px; background: var(--white); margin: 16px 0 18px;
  }
  .contact__list { list-style: none; font-family: "Lato", sans-serif; font-size: 15px; line-height: 1.35; }
  .contact__item { display: flex; gap: 9px; align-items: flex-start; margin-bottom: 5px; }
  .contact__icon { flex: 0 0 15px; width: 15px; height: 15px; margin-top: 2px; }
  .card-band {
    position: absolute; bottom: 0; height: 9px;
  }
  .card-band--blue { left: 0; width: 480px; background: var(--band-blue); }
  .card-band--yellow { left: 480px; right: 0; background: var(--brand-yellow); }
</style>
</head>
<body>
<main class="canvas">

  <section class="card card--front" aria-label="Card front">
    <div class="bees" role="img" aria-label="Two cartoon bees flying"></div>
    <div class="front-logo">LanternPips</div>
    <p class="front-web">WWW.<span class="accent">LANTERNPIPS-DEMO</span>.COM</p>
    <div class="sunflowers" role="img" aria-label="Sunflowers with a small bee beside the fence"></div>
    <div class="fence-scene" role="img" aria-label="White picket fence running across the bottom of the card"></div>
    <div class="house" role="img" aria-label="Small cream house with a red roof"></div>
  </section>

  <section class="card card--back" aria-label="Card back">
    <div class="back-logo">LanternPips</div>
    <div class="contact">
      <h1 class="contact__name">Mara Delwyn</h1>
      <p class="contact__title">Founder Creator</p>
      <div class="contact__rule"></div>
      <ul class="contact__list">
        <li class="contact__item">
          <svg class="contact__icon" viewBox="0 0 16 16"><rect x="3" y="1" width="10" height="14" rx="2" fill="var(--brand-yellow)"/><rect x="5" y="3" width="6" height="8" fill="var(--brand-red)"/></svg>
          <span>555 017 2869</span>
        </li>
        <li class="contact__item">
          <svg class="contact__icon" viewBox="0 0 16 16"><path d="M1 7 15 1 10 15 8 9Z" fill="var(--brand-yellow)"/></svg>
          <span>maradelwyn@quillpost-mail.com</span>
        </li>
        <li class="contact__item">
          <svg class="contact__icon" viewBox="0 0 16 16"><path d="M8 1a5 5 0 0 1 5 5c0 4-5 9-5 9S3 10 3 6a5 5 0 0 1 5-5z" fill="var(--brand-yellow)"/><circle cx="8" cy="6" r="2" fill="var(--brand-red)"/></svg>
          <span>4718 E Hollin Bend<br>Fernmoor, QX 70812</span>
        </li>
        <li class="contact__item">
          <svg class="contact__icon" viewBox="0 0 16 16"><circle cx="8" cy="8" r="7" fill="var(--brand-yellow)"/><path d="M1 8h14M8 1c-3 3-3 11 0 14M8 1c3 3 3 11 0 14" stroke="var(--brand-red)" stroke-width="1.2" fill="none"/></svg>
          <span>Patent Pending IP</span>
        </li>
      </ul>
    </div>
    <div class="card-band card-band--blue"></div>
    <div class="card-band card-band--yellow"></div>
  </section>

</main>
</body>
</html>
```